Website design with eCommerce for revolutionary new product in the manufacturing industry.

We need a website designed for a precision manufacturing company based in the suburbs of Minneapolis, Minnesota called Velkor Manufacturing. We have a revolutionary new product, the TRIM LATCH, to introduce and sell through an eCommerce storefront. The website would include company information, product information, and the storefront. Green is a color that represents Velkor Manufacturing. The final design should communicate that we exclusively offer premium products at a premium price. The design should also let the customer know they are the focus of our work.

Target Market(s)

Machinists and machine shops

Industry/Entity Type

Manufacturing and machine shops

Coding

Coded - Design and coding required

Font styles to use
Sans Serif

Colors
59FF00
82FF00
B8FF75
E3FFCB
F4FFEA

Requirements
Must have
• eCommerce storefront, Made in USA references
Nice to have
• Home page, TRIM LATCH Product page, About Us, Capabilities, Contact, etc.
Should not have
• Should not be too much text and reading.

```html
<!DOCTYPE html>
<html lang="en">
<head>
<meta charset="utf-8">
<title>Velkor Manufacturing</title>
<link href="https://fonts.googleapis.com/css2?family=Audiowide&family=Lato:wght@400;700&display=swap" rel="stylesheet">
<style>
:root{
  --lime:#8cff3c;
  --lime-bright:#59ff00;
  --lime-soft:#b8ff75;
  --lime-pale:#e3ffcb;
  --green-deep:#1f8a12;
  --ink:#111111;
  --text:#3a3a3a;
  --muted:#6b6b6b;
  --grey-bg:#eef0f1;
  --card-bg:#e4e6e8;
  --white:#ffffff;
  --star:#f4c20d;
}
*{box-sizing:border-box;margin:0;padding:0}
html,body{width:1200px;height:3299px;overflow:hidden;background:var(--white)}
body{font-family:"Lato",sans-serif;color:var(--text)}
.page{position:relative;width:1200px;height:3299px;overflow:hidden}
.abs{position:absolute}
.display{font-family:"Audiowide",sans-serif;color:var(--ink);font-weight:400;white-space:nowrap}
.pill{position:absolute;display:flex;align-items:center;justify-content:center;border-radius:40px;background:var(--lime);font-family:"Audiowide",sans-serif;color:var(--ink);font-size:18px}

/* header */
.topbar{left:326px;top:0;width:874px;height:42px;background:var(--lime);clip-path:polygon(60px 0,100% 0,100% 100%,0 100%)}
.topbar-item{position:absolute;top:11px;font-size:15px;color:var(--ink);display:flex;align-items:center;gap:8px}
.social{position:absolute;top:13px;display:flex;gap:9px}
.social span{width:14px;height:14px;border-radius:50%;background:var(--ink);display:block}
.brand{left:111px;top:30px;font-family:"Audiowide",sans-serif;font-size:26px;color:var(--ink);display:flex;align-items:center;gap:10px;line-height:1;white-space:nowrap}
.brand .dot{width:20px;height:20px;border-radius:50%;background:var(--lime-bright)}
.nav{position:absolute;top:68px;font-size:15px;color:#333}
.signup{left:956px;top:55px;width:132px;height:44px}

/* hero */
.hero{left:0;top:113px;width:1200px;height:655px;background:radial-gradient(ellipse at 30% 40%,#3a3d38 0%,#1e201d 55%,#0f100f 100%)}
.hero-title{left:113px;top:270px;font-size:35px;line-height:52px;color:var(--white)}
.hero-copy{left:113px;top:388px;width:440px;font-size:15px;line-height:23px;color:#e9e9e9}
.hero-btn{left:113px;top:458px;width:142px;height:48px}
.ring-outer{left:617px;top:166px;width:474px;height:474px;border-radius:50%;background:rgba(140,255,60,.45)}
.ring-inner{left:656px;top:205px;width:396px;height:396px;border-radius:50%;background:var(--lime)}
.hero-product{left:730px;top:250px;width:250px;height:320px;border-radius:18px;background:linear-gradient(150deg,#2fb01c,#106b0a)}

/* about */
.about{left:0;top:700px;width:1200px;height:544px;background:var(--grey-bg)}
.about-mark{left:110px;top:930px;font-family:"Audiowide",sans-serif;font-size:84px;line-height:1;color:var(--lime-bright)}
.about-mark small{display:block;font-size:46px;margin-top:18px;letter-spacing:4px}
.about-title{left:626px;top:832px;font-size:26px}
.about-copy{left:626px;top:885px;width:470px;font-size:15.5px;line-height:25.7px;color:var(--text)}
.about-btn{left:623px;top:1112px;width:160px;height:53px}

/* products */
.section-title{width:1200px;left:0;text-align:center;font-size:36px}
.card{position:absolute;top:1396px;width:227px;text-align:center}
.card-img{height:244px;border-radius:14px;background:linear-gradient(160deg,#4a4a47,#1f201e)}
.card-img.light{background:linear-gradient(160deg,#e8e9eb,#d3d5d7)}
.plus{position:absolute;left:88px;top:214px;width:50px;height:50px;border-radius:50%;background:var(--lime);display:flex;align-items:center;justify-content:center}
.card-name{margin-top:32px;font-family:"Audiowide",sans-serif;font-size:16px;color:var(--ink);white-space:nowrap;letter-spacing:-.2px}
.stars{margin-top:6px;color:var(--star);font-size:15px;letter-spacing:5px}
.price{margin-top:4px;font-family:"Audiowide",sans-serif;font-size:18px;color:var(--ink)}
.card .pill{position:relative;margin:10px auto 0;width:132px;height:38px;font-size:16px}

/* what we do */
.band{left:0;top:1884px;width:1200px;height:478px;background:var(--lime)}
.band-photo{left:430px;top:1884px;width:770px;height:478px;background:linear-gradient(90deg,rgba(140,255,60,1) 0%,rgba(140,255,60,.6) 25%,#8e9a7e 55%,#5f645a 80%,#3f423c 100%)}
.band-title{left:113px;top:1940px;font-size:37px}
.band-copy{left:113px;top:1993px;width:480px;font-size:15.5px;line-height:25.7px;color:#1c1c1c}
.band-btn{left:113px;top:2246px;width:160px;height:54px;background:var(--white)}

/* contact */
.info{position:absolute;left:113px;display:flex;gap:13px}
.info-icon{width:50px;height:50px;border-radius:50%;border:2px solid var(--lime-pale);display:flex;align-items:center;justify-content:center;flex:none}
.info h4{font-family:"Audiowide",sans-serif;font-weight:400;font-size:18px;color:var(--ink);margin-top:2px}
.info p{font-size:15px;line-height:24px;color:#333;margin-top:3px}
.field{position:absolute;left:457px;width:317px;height:53px;background:var(--white);box-shadow:0 2px 10px rgba(0,0,0,.12);font-size:15px;color:#8a8a8a;padding:16px 24px}
.submit{position:absolute;left:457px;top:2720px;width:317px;height:54px;background:var(--lime);font-family:"Audiowide",sans-serif;font-size:17px;color:var(--ink);display:flex;align-items:center;justify-content:center}
.message{position:absolute;left:795px;top:2515px;width:293px;height:259px;background:var(--white);box-shadow:0 2px 10px rgba(0,0,0,.12);font-size:15px;color:#8a8a8a;padding:17px 24px}

/* footer */
.footer{left:0;top:2930px;width:1200px;height:369px;background:var(--ink)}
.foot-brand{left:115px;top:3046px;font-family:"Audiowide",sans-serif;font-size:34px;color:var(--white);display:flex;align-items:center;gap:12px;white-space:nowrap}
.foot-brand .dot{width:24px;height:24px;border-radius:50%;background:var(--lime-bright)}
.foot-title{font-family:"Audiowide",sans-serif;font-weight:400;font-size:21px;color:var(--white);white-space:nowrap}
.foot-line{position:absolute;left:430px;display:flex;gap:10px;font-size:15px;line-height:23px;color:#eaeaea}
.newsletter{left:726px;top:3059px;width:345px;height:37px;border-radius:30px;background:var(--white)}
.newsletter span{position:absolute;left:18px;top:9px;font-size:15px;color:#777}
.newsletter b{position:absolute;right:0;top:0;width:130px;height:37px;border-radius:30px;background:var(--lime);font-family:"Audiowide",sans-serif;font-weight:400;font-size:17px;color:var(--ink);display:flex;align-items:center;justify-content:center}
.foot-social{left:736px;top:3134px;display:flex;gap:15px}
.foot-social span{width:14px;height:14px;border-radius:50%;background:var(--white);display:block}
.rule{left:110px;top:3210px;width:980px;height:1px;background:#333}
.legal{top:3245px;font-size:15px;color:#e6e6e6}
</style>
</head>
<body>
<div class="page">

  <!-- header -->
  <div class="abs topbar"></div>
  <div class="topbar-item" style="left:448px">
    <svg width="14" height="14" viewBox="0 0 24 24"><path d="M6.6 10.8a15 15 0 0 0 6.6 6.6l2.2-2.2c.3-.3.7-.4 1-.2 1.1.4 2.3.6 3.6.6.6 0 1 .4 1 1V20c0 .6-.4 1-1 1A17 17 0 0 1 3 4c0-.6.4-1 1-1h3.5c.6 0 1 .4 1 1 0 1.3.2 2.5.6 3.6.1.3 0 .7-.2 1z" fill="#111"/></svg>
    +1 888 888 8888
  </div>
  <div class="topbar-item" style="left:625px">
    <svg width="12" height="16" viewBox="0 0 24 32"><path d="M12 0a12 12 0 0 0-12 12c0 9 12 20 12 20s12-11 12-20A12 12 0 0 0 12 0zm0 17a5 5 0 1 1 0-10 5 5 0 0 1 0 10z" fill="#111"/></svg>
    Lorem ipsum dolor sit amet, consectetur
  </div>
  <div class="social" style="left:960px"><span></span><span></span><span></span><span></span></div>

  <div class="abs brand"><i class="dot"></i>Velkor MFG</div>
  <div class="nav" style="left:365px">Home</div>
  <div class="nav" style="left:461px">Our Product</div>
  <div class="nav" style="left:599px">About Us</div>
  <div class="nav" style="left:717px">Capabilities</div>
  <div class="nav" style="left:852px">Contact</div>
  <div class="pill signup">Sign Up</div>

  <!-- about background -->
  <div class="abs about"></div>

  <!-- hero -->
  <div class="abs hero" role="img" aria-label="Close-up of dark metal machining shavings"></div>
  <svg class="abs" style="left:0;top:640px" width="1200" height="140" viewBox="0 0 1200 140">
    <path d="M0 40 C180 110 330 130 520 80 C700 30 780 20 900 50 C1020 80 1120 90 1200 40 V140 H0Z" fill="#eef0f1"/>
    <path d="M0 40 C180 110 330 130 520 80 C700 30 780 20 900 50 C1020 80 1120 90 1200 40" fill="none" stroke="#8cff3c" stroke-width="12"/>
    <path d="M0 25 C180 92 330 112 520 62 C700 12 780 2 900 32 C1020 62 1120 72 1200 22 V40 C1120 90 1020 80 900 50 C780 20 700 30 520 80 C330 130 180 110 0 40Z" fill="#ffffff"/>
  </svg>
  <h1 class="abs display hero-title">Welcome To<br>Velkor Manufacturing</h1>
  <p class="abs hero-copy">Lorem ipsum dolor sit amet, consectetur adipiscing elit, sed do eiusmod tempor incididunt ut labore et</p>
  <div class="pill hero-btn">Get Started</div>
  <div class="abs ring-outer"></div>
  <div class="abs ring-inner"></div>
  <div class="abs hero-product" role="img" aria-label="Green anodized TRIM LATCH machinist stop with steel pin"></div>

  <!-- about -->
  <div class="abs about-mark">Velkor<small>MFG</small></div>
  <h2 class="abs display about-title">Velkor Manufacturing About</h2>
  <p class="abs about-copy">Velkor Manufacturing has humble roots, starting as many machine shops do, in a home garage. The chance purchase of a CNC machining center started the journey, and the continued need for detailed solutions keeps it going and growing. Here, you will meet the people who have made Velkor Manufacturing what it is today. While they have learned a great deal from many other talented individuals, it is their specific interpretation and application of that knowledge that creates a dynamic level of execution.</p>
  <div class="pill about-btn">Learn More</div>

  <!-- products -->
  <h2 class="abs display section-title" style="top:1310px">Our Product</h2>

  <div class="card" style="left:111px">
    <div class="card-img light" role="img" aria-label="TRIM LATCH stop on a light background"></div>
    <div class="plus"><svg width="18" height="18" viewBox="0 0 18 18"><path d="M9 2v14M2 9h14" stroke="#fff" stroke-width="3"/></svg></div>
    <div class="card-name">Trim Latch Kit 001</div>
    <div class="stars">★★★★★</div>
    <div class="price">$56.00</div>
    <div class="pill">Shop Now</div>
  </div>
  <div class="card" style="left:362px">
    <div class="card-img" role="img" aria-label="TRIM LATCH kit in a foam case with tools"></div>
    <div class="plus"><svg width="18" height="18" viewBox="0 0 18 18"><path d="M9 2v14M2 9h14" stroke="#fff" stroke-width="3"/></svg></div>
    <div class="card-name">TLK-001a</div>
    <div class="stars">★★★★★</div>
    <div class="price">$56.00</div>
    <div class="pill">Shop Now</div>
  </div>
  <div class="card" style="left:612px">
    <div class="card-img" role="img" aria-label="TRIM LATCH kit in a foam case with tools"></div>
    <div class="plus"><svg width="18" height="18" viewBox="0 0 18 18"><path d="M9 2v14M2 9h14" stroke="#fff" stroke-width="3"/></svg></div>
    <div class="card-name">TLK-002a</div>
    <div class="stars">★★★★★</div>
    <div class="price">$56.00</div>
    <div class="pill">Shop Now</div>
  </div>
  <div class="card" style="left:863px">
    <div class="card-img" role="img" aria-label="Two TRIM LATCH stops in a foam case with tools"></div>
    <div class="plus"><svg width="18" height="18" viewBox="0 0 18 18"><path d="M9 2v14M2 9h14" stroke="#fff" stroke-width="3"/></svg></div>
    <div class="card-name">Trim Latch Kit 003a</div>
    <div class="stars">★★★★★</div>
    <div class="price">$56.00</div>
    <div class="pill">Shop Now</div>
  </div>

  <!-- what we do -->
  <div class="abs band"></div>
  <div class="abs band-photo" role="img" aria-label="Pile of bright metal machining chips"></div>
  <h2 class="abs display band-title">What we do</h2>
  <p class="abs band-copy">We are a machine shop with complete end to end manufacturing capabilities. We can take an idea or need, and bring it to a complete physical product. We can design and build your prototype, and we can mass produce it too. We love working directly with customers to manufacture their products, and help make it better where appropriate. We can work with as little as a verbal description, up to following fully defined customer specifications. We work in a wide variety of materials, and are very good at creating fixture designs to address your process issues.</p>
  <div class="pill band-btn">Learn More</div>

  <!-- contact -->
  <h2 class="abs display section-title" style="top:2431px">Contact Us</h2>

  <div class="info" style="top:2516px">
    <div class="info-icon"><svg width="12" height="16" viewBox="0 0 24 32"><path d="M12 0a12 12 0 0 0-12 12c0 9 12 20 12 20s12-11 12-20A12 12 0 0 0 12 0zm0 17a5 5 0 1 1 0-10 5 5 0 0 1 0 10z" fill="#8cff3c"/></svg></div>
    <div><h4>Location</h4><p>Lorem ipsum dolor sit amet, con-<br>sectetur adipiscing elit</p></div>
  </div>
  <div class="info" style="top:2620px">
    <div class="info-icon"><svg width="14" height="14" viewBox="0 0 24 24"><path d="M6.6 10.8a15 15 0 0 0 6.6 6.6l2.2-2.2c.3-.3.7-.4 1-.2 1.1.4 2.3.6 3.6.6.6 0 1 .4 1 1V20c0 .6-.4 1-1 1A17 17 0 0 1 3 4c0-.6.4-1 1-1h3.5c.6 0 1 .4 1 1 0 1.3.2 2.5.6 3.6.1.3 0 .7-.2 1z" fill="#8cff3c"/></svg></div>
    <div><h4>Phone</h4><p>+1 888 888 8888</p></div>
  </div>
  <div class="info" style="top:2716px">
    <div class="info-icon"><svg width="15" height="11" viewBox="0 0 30 22"><rect width="30" height="22" rx="2" fill="#8cff3c"/><path d="M1 2l14 11L29 2" fill="none" stroke="#fff" stroke-width="2.5"/></svg></div>
    <div><h4>Email</h4><p>info@velkormfg.com</p></div>
  </div>

  <div class="field" style="top:2515px">Name</div>
  <div class="field" style="top:2583px">Phone</div>
  <div class="field" style="top:2651px">Email</div>
  <div class="submit">Submit</div>
  <div class="message">Type your message</div>

  <!-- footer -->
  <svg class="abs" style="left:0;top:2840px" width="1200" height="100" viewBox="0 0 1200 100">
    <path d="M0 78 C200 0 380 20 560 70 C720 110 900 40 1040 10 C1110 -5 1170 20 1200 40 V100 H0Z" fill="#8cff3c"/>
    <path d="M0 92 C200 20 380 40 560 90 C720 125 900 60 1040 30 C1110 15 1170 40 1200 58 V100 H0Z" fill="#ffffff"/>
  </svg>
  <svg class="abs" style="left:0;top:2860px" width="1200" height="80" viewBox="0 0 1200 80">
    <path d="M0 84 C200 16 380 36 560 84 C720 118 900 56 1040 28 C1110 14 1170 38 1200 54 V80 H0Z" fill="#111111"/>
  </svg>
  <div class="abs footer"></div>

  <div class="abs foot-brand"><i class="dot"></i>Velkor MFG</div>

  <h3 class="abs foot-title" style="left:430px;top:3005px">Contact Us</h3>
  <div class="foot-line" style="top:3053px">
    <svg width="11" height="15" viewBox="0 0 24 32" style="margin-top:3px;flex:none"><path d="M12 0a12 12 0 0 0-12 12c0 9 12 20 12 20s12-11 12-20A12 12 0 0 0 12 0zm0 17a5 5 0 1 1 0-10 5 5 0 0 1 0 10z" fill="#fff"/></svg>
    <span>Lorem ipsum dolor sit amet,<br>consectetur adipiscing elit, sed</span>
  </div>
  <div class="foot-line" style="top:3107px">
    <svg width="13" height="13" viewBox="0 0 24 24" style="margin-top:5px"><path d="M6.6 10.8a15 15 0 0 0 6.6 6.6l2.2-2.2c.3-.3.7-.4 1-.2 1.1.4 2.3.6 3.6.6.6 0 1 .4 1 1V20c0 .6-.4 1-1 1A17 17 0 0 1 3 4c0-.6.4-1 1-1h3.5c.6 0 1 .4 1 1 0 1.3.2 2.5.6 3.6.1.3 0 .7-.2 1z" fill="#fff"/></svg>
    <span>+1 888 888 8888</span>
  </div>
  <div class="foot-line" style="top:3145px">
    <svg width="14" height="10" viewBox="0 0 30 22" style="margin-top:7px"><rect width="30" height="22" rx="2" fill="#fff"/><path d="M1 2l14 11L29 2" fill="none" stroke="#111" stroke-width="2.5"/></svg>
    <span>info@velkormfg.com</span>
  </div>

  <h3 class="abs foot-title" style="left:726px;top:3005px">Subscribe To Our Newsletter</h3>
  <div class="abs newsletter"><span>Enter Your Email</span><b>Subscribe</b></div>
  <div class="abs foot-social"><span></span><span></span><span></span><span></span></div>

  <div class="abs rule"></div>
  <div class="abs legal" style="left:110px">© Copyrights 2022 Velkor Manufacturing| &nbsp;&nbsp; All Rights Reserved</div>
  <div class="abs legal" style="left:724px">Terms&amp;condtions | Privacy Policy | About Us Support</div>

</div>
</body>
</html>
```